Website for Vetra Kolan Holdings

Need a project marketing website for our company which primarily deals in selling real estate(land sales) from Big Estates to Builders /Clients, help them in Building & Construction and do all Project Management.

Coding

Coded - Design and coding required

Number of Pages Required

4 page

Colors
0054AA
0677BA
7BADD7
CADEEF
E8F1F8
FFC000
F8CF3A
FAE287
FDF2CF
FEFAEE

```html
<!DOCTYPE html>
<html lang="en">
<head>
<meta charset="utf-8">
<title>Vetra Kolan Holdings</title>
<link href="https://fonts.googleapis.com/css2?family=Poppins:wght@400;500;600;700;800&display=swap" rel="stylesheet">
<style>
:root{
  --navy:#0a1430;
  --navy-2:#14254f;
  --blue:#0054AA;
  --yellow:#FFC000;
  --yellow-2:#F8CF3A;
  --cream:#FDF2CF;
  --cream-2:#FEFAEE;
  --ink:#1b1b1b;
  --muted:#5a5f6b;
  --white:#ffffff;
}
*{box-sizing:border-box;margin:0;padding:0}
html,body{width:1200px;height:3860px;overflow:hidden}
body{font-family:"Poppins",sans-serif;color:var(--ink);background:var(--white);position:relative}
.btn{display:inline-block;background:var(--yellow);color:var(--ink);font-weight:600;font-size:15px;border-radius:22px;padding:10px 26px;text-transform:uppercase;letter-spacing:.3px}
.brand{display:flex;align-items:center;gap:12px}
.brand-dot{width:36px;height:36px;border-radius:50%;background:var(--yellow)}
.brand-name{font-weight:700;font-size:17px;line-height:1.15;text-transform:uppercase;width:130px}

/* header */
.site-header{position:absolute;top:0;left:0;width:1200px;height:96px;background:var(--white);display:flex;align-items:center;padding:0 95px 0 45px;justify-content:space-between;z-index:3}
.site-header .brand-name{color:var(--navy)}
.main-nav{display:flex;gap:30px;margin-left:190px;font-size:16px;font-weight:500}
.site-header .btn{font-size:14px;padding:8px 22px}

/* hero */
.hero{position:absolute;top:96px;left:0;width:1200px;height:770px;background:linear-gradient(180deg,#1a2752 0%,#0f1a3e 55%,#0a1430 100%);overflow:hidden}
.hero-city{position:absolute;inset:0;background:linear-gradient(90deg,rgba(40,60,110,.45),rgba(20,35,75,.2) 60%,rgba(30,50,95,.4))}
.hero-people{position:absolute;left:640px;top:50px;width:560px;height:560px;background:radial-gradient(ellipse at 50% 45%,#c9ccd3 0%,#7f8797 45%,#2e3a5c 80%,transparent 100%)}
.hero-copy{position:absolute;left:55px;top:165px;width:560px;color:var(--white)}
.hero-copy h1{font-size:42px;font-weight:700;line-height:1.18;text-transform:uppercase;letter-spacing:.5px}
.hero-copy p{font-size:13px;line-height:1.45;margin:16px 0 28px;color:#d7dcea;width:470px}
.hero-wave{position:absolute;left:0;bottom:0;width:1200px;height:200px}

/* features */
.features{position:absolute;top:955px;left:0;width:1200px;display:flex;justify-content:center;gap:30px}
.feature-card{width:255px;height:310px;background:var(--white);border-radius:8px;box-shadow:0 10px 35px rgba(10,20,48,.12);text-align:center;padding:30px 22px}
.feature-icon{width:100px;height:100px;border-radius:50%;background:var(--yellow);margin:0 auto 22px;display:flex;align-items:center;justify-content:center}
.feature-card h3{font-size:16px;font-weight:600;margin-bottom:12px}
.feature-card p{font-size:13px;line-height:1.5;color:var(--muted)}

/* about */
.about-photo-wrap{position:absolute;left:75px;top:1400px;width:450px;height:450px}
.about-photo{position:absolute;inset:10px;border-radius:50%;background:linear-gradient(180deg,#cfe1f1 0%,#9fbfdb 40%,#6f8aa6 75%,#4c6078 100%)}
.about-ring{position:absolute;inset:0}
.about-copy{position:absolute;left:625px;top:1490px;width:470px}
.about-copy h2{font-size:42px;font-weight:700;text-transform:uppercase;margin-bottom:14px}
.about-copy p{font-size:13px;line-height:1.5;color:var(--muted);margin-bottom:26px}

/* services */
.services{position:absolute;top:2020px;left:0;width:1200px;height:780px;background:linear-gradient(180deg,var(--cream) 0%,var(--cream-2) 55%,var(--white) 100%)}
.services h2{position:absolute;top:125px;width:100%;text-align:center;font-size:40px;font-weight:700;text-transform:uppercase}
.service-list{position:absolute;top:260px;left:140px;display:flex;gap:50px}
.service-card{width:270px;height:380px;background:var(--white);border-radius:12px;box-shadow:0 10px 30px rgba(10,20,48,.1);overflow:hidden;text-align:center}
.service-photo{height:195px}
.service-card h3{font-size:17px;font-weight:600;margin:18px 14px 8px;line-height:1.25}
.service-card p{font-size:12px;line-height:1.45;color:var(--muted);padding:0 20px;margin-bottom:14px}
.service-card .btn{font-size:13px;padding:7px 22px}
.slider-arrow{position:absolute;top:395px;width:50px;height:40px}
.slider-arrow.prev{left:50px}
.slider-arrow.next{right:50px}

/* testimonials */
.testimonials h2{position:absolute;top:2830px;width:100%;text-align:center;font-size:38px;font-weight:700;text-transform:uppercase}
.quote{position:absolute;top:2950px;width:450px}
.quote.left{left:180px}
.quote.right{left:650px}
.stars{display:flex;gap:8px;margin-bottom:16px}
.quote blockquote{font-size:21px;line-height:1.35;color:#3b3f4a;margin-bottom:24px}
.author{display:flex;align-items:center;gap:20px}
.avatar{width:64px;height:64px;border-radius:50%;background:radial-gradient(circle at 50% 40%,#e7c7b2,#b07a5a 70%,#6e4632)}
.author strong{display:block;font-size:17px;font-weight:600;text-transform:uppercase}
.author span{font-size:16px;color:var(--muted)}

/* footer */
.site-footer{position:absolute;top:3380px;left:0;width:1200px;height:480px}
.footer-wave{position:absolute;top:0;left:0;width:1200px;height:120px}
.footer-body{position:absolute;top:110px;left:0;width:1200px;height:370px;background:var(--navy);color:var(--white)}
.footer-brand{position:absolute;left:90px;top:70px}
.footer-brand .brand-name{color:var(--white);font-size:18px}
.socials{display:flex;gap:14px;margin-top:28px}
.socials span{width:26px;height:26px;border-radius:50%;background:var(--yellow)}
.footer-col{position:absolute;top:40px}
.footer-col h4{font-size:15px;font-weight:600;text-transform:uppercase;margin-bottom:22px;letter-spacing:.5px}
.footer-col ul{list-style:none;font-size:14px}
.footer-col li{margin-bottom:15px}
.col-links{left:385px}
.col-contact{left:580px;width:280px}
.contact-row{display:flex;gap:16px;font-size:14px;margin-bottom:18px;line-height:1.4}
.contact-row svg{flex:0 0 18px;margin-top:2px}
.col-news{left:920px;width:220px;text-align:center}
.news-input{height:36px;border-radius:18px;background:var(--navy-2);border:1px solid #2d3e6e;font-size:12px;color:#b9c2dc;display:flex;align-items:center;justify-content:center;margin-bottom:12px}
.col-news .btn{font-size:12px;padding:8px 26px}
.copyright{position:absolute;bottom:22px;width:100%;text-align:center;font-size:11px;color:#b9c2dc}
</style>
</head>
<body>

<header class="site-header">
  <div class="brand"><span class="brand-dot"></span><span class="brand-name">Vetra Kolan Holdings</span></div>
  <nav class="main-nav"><span>Home</span><span>About</span><span>Services</span><span>Blog</span><span>Contact</span></nav>
  <span class="btn">Get a Quote</span>
</header>

<section class="hero">
  <div class="hero-city" role="img" aria-label="Night city skyline with high-rise towers"></div>
  <div class="hero-people" role="img" aria-label="Team of business professionals reviewing documents"></div>
  <div class="hero-copy">
    <h1>We market and deliver your real estate vision</h1>
    <p>Achieve lasting property growth with tailored land sales, marketing strategy and project delivery, guided by a team that plans every stage with you.</p>
    <span class="btn">Get a Quote</span>
  </div>
  <svg class="hero-wave" viewBox="0 0 1200 200" preserveAspectRatio="none">
    <path d="M0 150 C300 200 700 190 1200 60 L1200 200 L0 200 Z" fill="#FFC000"/>
    <path d="M0 168 C320 210 720 205 1200 85 L1200 200 L0 200 Z" fill="#ffffff"/>
  </svg>
</section>

<section class="features">
  <article class="feature-card">
    <div class="feature-icon"><svg width="54" height="54" viewBox="0 0 54 54" fill="none" stroke="#1b1b1b" stroke-width="3"><path d="M8 46h38M13 46V32M23 46V24M33 46V28M43 46V14M10 26l12-10 10 6 14-12"/></svg></div>
    <h3>Increased Profitability</h3>
    <p>Strategic investments in assets, marketing, or product development can generate higher returns.</p>
  </article>
  <article class="feature-card">
    <div class="feature-icon"><svg width="54" height="54" viewBox="0 0 54 54" fill="none" stroke="#1b1b1b" stroke-width="3"><circle cx="27" cy="20" r="8"/><path d="M12 44c2-9 8-14 15-14s13 5 15 14M8 30l6-6M46 30l-6-6"/></svg></div>
    <h3>Competitive Advantage</h3>
    <p>Strategic investments in assets, marketing, or product development can generate higher returns.</p>
  </article>
  <article class="feature-card">
    <div class="feature-icon"><svg width="54" height="54" viewBox="0 0 54 54" fill="none" stroke="#1b1b1b" stroke-width="3"><rect x="8" y="34" width="8" height="12"/><rect x="22" y="26" width="8" height="20"/><rect x="36" y="18" width="8" height="28"/><path d="M8 22l12-8 8 4 16-10"/></svg></div>
    <h3>Wealth Accumulation</h3>
    <p>Strategic investments in assets, marketing, or product development can generate higher returns.</p>
  </article>
</section>

<section class="about">
  <div class="about-photo-wrap">
    <svg class="about-ring" viewBox="0 0 450 450"><path d="M225 5 A220 220 0 0 1 445 225" fill="none" stroke="#FFC000" stroke-width="10"/><path d="M5 225 A220 220 0 0 0 225 445" fill="none" stroke="#FFC000" stroke-width="10"/></svg>
    <div class="about-photo" role="img" aria-label="Modern residential towers against a pale sky"></div>
  </div>
  <div class="about-copy">
    <h2>About Us</h2>
    <p>We connect large estate owners with builders and private clients, guiding every land sale from first valuation to final settlement. Our team then stays involved through design, approvals and construction, managing schedules, budgets and contractors so each project is delivered on time. With deep local knowledge and a clear marketing approach, we help landholders unlock value and help builders secure sites ready for growth, while keeping every partner informed at each stage of the journey ahead.</p>
    <span class="btn">Read More</span>
  </div>
</section>

<section class="services">
  <h2>Our Services</h2>
  <svg class="slider-arrow prev" viewBox="0 0 50 40"><path d="M46 20H6M20 6L6 20l14 14" fill="none" stroke="#1b1b1b" stroke-width="4"/></svg>
  <div class="service-list">
    <article class="service-card">
      <div class="service-photo" role="img" aria-label="Business handshake over a land deal" style="background:linear-gradient(135deg,#2d3b57,#7a8aa3 60%,#c9d3df)"></div>
      <h3>Land Sales &amp; Acquisition</h3>
      <p>We match estate land with builders and buyers, handling pricing, listing and settlement with care.</p>
      <span class="btn">View More</span>
    </article>
    <article class="service-card">
      <div class="service-photo" role="img" aria-label="Colleagues planning a marketing campaign at a desk" style="background:linear-gradient(135deg,#d8cdbf,#9c8f84 55%,#4a4a55)"></div>
      <h3>Project Marketing</h3>
      <p>Launch campaigns, sales suites and buyer outreach that bring new developments to the right market.</p>
      <span class="btn">View More</span>
    </article>
    <article class="service-card">
      <div class="service-photo" role="img" aria-label="Project manager working on a laptop in an office" style="background:linear-gradient(135deg,#e6e9ee,#aeb6c2 55%,#5d6777)"></div>
      <h3>Construction Support</h3>
      <p>From approvals to handover, we manage trades, timelines and budgets so every build stays on track.</p>
      <span class="btn">View More</span>
    </article>
  </div>
  <svg class="slider-arrow next" viewBox="0 0 50 40"><path d="M4 20h40M30 6l14 14-14 14" fill="none" stroke="#1b1b1b" stroke-width="4"/></svg>
</section>

<section class="testimonials">
  <h2>What Client Say’s</h2>
  <article class="quote left">
    <div class="stars">
      <svg width="22" height="22" viewBox="0 0 24 24"><path d="M12 2l3 7 7 .6-5.3 4.7 1.6 7.2L12 17.8 5.7 21.5l1.6-7.2L2 9.6 9 9z" fill="#FFC000"/></svg><svg width="22" height="22" viewBox="0 0 24 24"><path d="M12 2l3 7 7 .6-5.3 4.7 1.6 7.2L12 17.8 5.7 21.5l1.6-7.2L2 9.6 9 9z" fill="#FFC000"/></svg><svg width="22" height="22" viewBox="0 0 24 24"><path d="M12 2l3 7 7 .6-5.3 4.7 1.6 7.2L12 17.8 5.7 21.5l1.6-7.2L2 9.6 9 9z" fill="#FFC000"/></svg><svg width="22" height="22" viewBox="0 0 24 24"><path d="M12 2l3 7 7 .6-5.3 4.7 1.6 7.2L12 17.8 5.7 21.5l1.6-7.2L2 9.6 9 9z" fill="#FFC000"/></svg><svg width="22" height="22" viewBox="0 0 24 24"><path d="M12 2l3 7 7 .6-5.3 4.7 1.6 7.2L12 17.8 5.7 21.5l1.6-7.2L2 9.6 9 9z" fill="#FFC000"/></svg>
    </div>
    <blockquote>The sales dashboards are fantastic! They provide clear, real-time insights into our performance, which has sparked healthy competition within our office. Everyone is motivated to reach their targets, and our sales numbers have never been better!</blockquote>
    <div class="author"><div class="avatar" role="img" aria-label="Client portrait"></div><div><strong>Tomas K.</strong><span>Owner</span></div></div>
  </article>
  <article class="quote right">
    <div class="stars">
      <svg width="22" height="22" viewBox="0 0 24 24"><path d="M12 2l3 7 7 .6-5.3 4.7 1.6 7.2L12 17.8 5.7 21.5l1.6-7.2L2 9.6 9 9z" fill="#FFC000"/></svg><svg width="22" height="22" viewBox="0 0 24 24"><path d="M12 2l3 7 7 .6-5.3 4.7 1.6 7.2L12 17.8 5.7 21.5l1.6-7.2L2 9.6 9 9z" fill="#FFC000"/></svg><svg width="22" height="22" viewBox="0 0 24 24"><path d="M12 2l3 7 7 .6-5.3 4.7 1.6 7.2L12 17.8 5.7 21.5l1.6-7.2L2 9.6 9 9z" fill="#FFC000"/></svg><svg width="22" height="22" viewBox="0 0 24 24"><path d="M12 2l3 7 7 .6-5.3 4.7 1.6 7.2L12 17.8 5.7 21.5l1.6-7.2L2 9.6 9 9z" fill="#FFC000"/></svg><svg width="22" height="22" viewBox="0 0 24 24"><path d="M12 2l3 7 7 .6-5.3 4.7 1.6 7.2L12 17.8 5.7 21.5l1.6-7.2L2 9.6 9 9z" fill="#FFC000"/></svg>
    </div>
    <blockquote>The sales dashboards are fantastic! They provide clear, real-time insights into our performance, which has sparked healthy competition within our office. Everyone is motivated to reach their targets, and our sales numbers have never been better!</blockquote>
    <div class="author"><div class="avatar" role="img" aria-label="Client portrait"></div><div><strong>Tomas K.</strong><span>Owner</span></div></div>
  </article>
</section>

<footer class="site-footer">
  <svg class="footer-wave" viewBox="0 0 1200 120" preserveAspectRatio="none">
    <path d="M0 40 C350 120 800 110 1200 20 L1200 120 L0 120 Z" fill="#FFC000"/>
    <path d="M0 58 C360 132 810 126 1200 40 L1200 120 L0 120 Z" fill="#0a1430"/>
  </svg>
  <div class="footer-body">
    <div class="footer-brand">
      <div class="brand"><span class="brand-dot"></span><span class="brand-name">Vetra Kolan Holdings</span></div>
      <div class="socials"><span></span><span></span><span></span></div>
    </div>
    <div class="footer-col col-links">
      <h4>Quick Links</h4>
      <ul><li>Home</li><li>Services</li><li>Pricing</li><li>About</li><li>Contact</li></ul>
    </div>
    <div class="footer-col col-contact">
      <h4>Contact Info</h4>
      <div class="contact-row"><svg width="18" height="18" viewBox="0 0 24 24"><path d="M6 2h4l2 5-3 2a12 12 0 0 0 6 6l2-3 5 2v4a2 2 0 0 1-2 2A18 18 0 0 1 4 4a2 2 0 0 1 2-2z" fill="#FFC000"/></svg><span>(000) 555 0142</span></div>
      <div class="contact-row"><svg width="18" height="18" viewBox="0 0 24 24"><rect x="2" y="5" width="20" height="14" rx="2" fill="#FFC000"/><path d="M3 6l9 7 9-7" fill="none" stroke="#0a1430" stroke-width="2"/></svg><span>hello@vetrakolan.com</span></div>
      <div class="contact-row"><svg width="18" height="18" viewBox="0 0 24 24"><path d="M12 2a7 7 0 0 0-7 7c0 5 7 13 7 13s7-8 7-13a7 7 0 0 0-7-7z" fill="#FFC000"/><circle cx="12" cy="9" r="2.5" fill="#0a1430"/></svg><span>Level 3, 88 Marlow Road, Eastbrook, Queensland 4000</span></div>
    </div>
    <div class="footer-col col-news">
      <h4>Stay Up-to-Date</h4>
      <div class="news-input">Email Address</div>
      <span class="btn">Subscribe Now</span>
    </div>
    <p class="copyright">© 2025 Vetra Kolan Holdings. All rights reserved.</p>
  </div>
</footer>

</body>
</html>
```